TernQuay Business Cards

Create business cards for our exciting new software company. We provide cloud billing systems and provisioning software for campany that need monthly SaaS and Cloud Billing

Target Market(s)

Enterprise businesses, b2b, telecom carriers, software manufactures

Industry/Entity Type

Software

```html
<!DOCTYPE html>
<html lang="en">
<head>
<meta charset="utf-8">
<title>TernQuay Business Cards</title>
<link rel="stylesheet" href="https://fonts.googleapis.com/css2?family=Open+Sans:wght@400;600;700&display=swap">
<style>
  :root {
    --backdrop: #e9ebee;
    --card-white: #f7f7f7;
    --navy: #1d4a78;
    --navy-deep: #143a63;
    --navy-light: #2a5d8f;
    --sky: #a9d6ea;
    --name-blue: #8fc6e3;
    --text-grey: #4a5563;
    --tag-grey: #7a8591;
  }
  * { margin: 0; padding: 0; box-sizing: border-box; }
  html, body { width: 1200px; height: 1023px; overflow: hidden; }
  body {
    background: var(--backdrop);
    font-family: "Open Sans", Arial, sans-serif;
    position: relative;
  }
  .card {
    position: absolute;
    left: 280px;
    width: 640px;
    height: 366px;
    border-radius: 26px;
    overflow: hidden;
    box-shadow: 0 10px 28px rgba(20, 40, 70, 0.18);
  }
  .card-front { top: 110px; background: var(--card-white); }
  .card-back {
    top: 547px;
    background: radial-gradient(ellipse at 40% 30%, var(--navy-light), var(--navy-deep) 75%);
  }

  /* Front */
  .bottom-band {
    position: absolute; left: 0; right: 0; bottom: 0; height: 22px;
    background: var(--navy);
  }
  .name-tab {
    position: absolute; left: 0; bottom: 22px;
    width: 300px; height: 92px;
    background: var(--navy);
    clip-path: polygon(0 0, 88% 0, 100% 50%, 100% 100%, 0 100%);
    padding: 18px 0 0 34px;
  }
  .person-name { color: var(--name-blue); font-weight: 700; font-size: 25px; line-height: 1.1; }
  .person-title { color: #dbe7f2; font-size: 15px; margin-top: 6px; }

  .brand {
    position: absolute; left: 300px; top: 70px;
    display: flex; flex-direction: column; align-items: flex-start;
  }
  .brand-row { display: flex; align-items: center; gap: 12px; }
  .brand-dot { width: 16px; height: 16px; border-radius: 50%; background: var(--navy); }
  .brand-name { font-size: 54px; font-weight: 600; color: var(--navy); line-height: 1; letter-spacing: -1px; }
  .brand-tag {
    margin-top: 8px; margin-left: 28px;
    font-size: 10.5px; letter-spacing: 1.6px; text-transform: uppercase;
    color: var(--tag-grey); line-height: 1.5;
  }

  .contact-list {
    position: absolute; left: 400px; bottom: 44px;
    list-style: none;
  }
  .contact-list li {
    display: flex; align-items: center; gap: 10px;
    font-size: 14px; color: var(--text-grey); line-height: 24px;
  }
  .contact-list svg { width: 13px; height: 13px; fill: var(--navy); flex: none; }

  /* Back */
  .back-brand {
    position: absolute; left: 0; right: 0; top: 120px;
    display: flex; flex-direction: column; align-items: center;
  }
  .back-brand .brand-dot { background: var(--sky); }
  .back-brand .brand-name { color: var(--sky); font-size: 62px; }
  .back-brand .brand-tag { color: var(--sky); margin-left: 0; text-align: center; font-size: 11.5px; }
</style>
</head>
<body>

<section class="card card-front" aria-label="Business card front">
  <div class="brand">
    <div class="brand-row">
      <span class="brand-dot"></span>
      <span class="brand-name">TernQuay</span>
    </div>
    <div class="brand-tag">Cloud billing and<br>operational support systems</div>
  </div>

  <ul class="contact-list">
    <li><svg viewBox="0 0 16 16"><path d="M4 1l3 3-2 2c1 2 3 4 5 5l2-2 3 3-2 3C7 15 1 9 1 3z"/></svg>+0 000 000 0000</li>
    <li><svg viewBox="0 0 16 16"><path d="M2 3h12v10H2zM4 5v2h8V5zM4 9v2h2V9zm3 0v2h2V9zm3 0v2h2V9z"/></svg>+0 000 000 0000</li>
    <li><svg viewBox="0 0 16 16"><path d="M1 3h14v10H1zm1.5 1.5L8 9l5.5-4.5z"/></svg>mellery@ternquay.com</li>
    <li><svg viewBox="0 0 16 16"><path d="M8 1a7 7 0 100 14A7 7 0 008 1zm0 1.5c.8 1 1.4 2.4 1.6 4H6.4C6.6 4.9 7.2 3.5 8 2.5zM2.6 7.5h2.3c.1 1.6.6 3 1.3 4.2A5.5 5.5 0 012.6 8.5zm0-1a5.5 5.5 0 013.6-4.2c-.7 1.2-1.2 2.6-1.3 4.2zm3.8 2h3.2c-.2 1.6-.8 3-1.6 4-.8-1-1.4-2.4-1.6-4zm4.7-2c-.1-1.6-.6-3-1.3-4.2a5.5 5.5 0 013.6 4.2zm0 1h2.3a5.5 5.5 0 01-3.6 4.2c.7-1.2 1.2-2.6 1.3-4.2z"/></svg>www.ternquay.com</li>
  </ul>

  <div class="name-tab">
    <div class="person-name">Marcus Ellery</div>
    <div class="person-title">President &amp; CEO</div>
  </div>
  <div class="bottom-band"></div>
</section>

<section class="card card-back" aria-label="Business card back">
  <div class="back-brand">
    <div class="brand-row">
      <span class="brand-dot"></span>
      <span class="brand-name">TernQuay</span>
    </div>
    <div class="brand-tag">Cloud billing and<br>operational support systems</div>
  </div>
</section>

</body>
</html>
```